Love pets? Create a veterinary business card that aligns with our new revamped website.

Greetings! We are a five-doctor veterinary hospital that seeks your expertise in designing a new business card that harmonizes with our recently revitalized website: www.tqrn.net. The card should feature our logo, the five doctors, operating hours, contact information, and communicate our purpose and personality.

Contact Information for Business Card

TBA

```html
<!DOCTYPE html>
<html lang="en">
<head>
<meta charset="utf-8">
<title>Maple Hollow Veterinary Hospital – Business Card</title>
<link rel="stylesheet" href="https://fonts.googleapis.com/css2?family=Montserrat:wght@400;500;700&family=Roboto:wght@400&display=swap">
<style>
  :root {
    --bg: #3b3d41;
    --card: #ffffff;
    --green: #3f8a2e;
    --leaf: #4a8f3f;
    --brown: #8a6418;
    --bark: #7a5a22;
    --amber: #d9952e;
    --slate: #728e9c;
    --grey: #5f5f5f;
  }
  * { margin: 0; padding: 0; box-sizing: border-box; }
  html, body { width: 1200px; height: 952px; overflow: hidden; }
  body {
    background: var(--bg);
    font-family: "Montserrat", sans-serif;
    position: relative;
  }
  .card {
    position: absolute;
    top: 326px;
    width: 520px;
    height: 300px;
    background: var(--card);
    border-radius: 18px;
    overflow: hidden;
    box-shadow: 0 10px 26px rgba(0,0,0,.35);
  }
  .card--front { left: 50px; }
  .card--back { left: 630px; }

  .artwork {
    position: absolute;
    z-index: 0;
    border-radius: 40% 40% 6px 6px;
    background: linear-gradient(180deg, var(--leaf) 0%, var(--leaf) 45%, var(--bark) 62%, var(--amber) 85%, var(--slate) 100%);
    opacity: .9;
  }
  .card--front .artwork { left: 20px; bottom: 0; width: 200px; height: 250px; }
  .card--back .artwork { right: 90px; bottom: 0; width: 140px; height: 130px; }

  .brand {
    position: absolute;
    z-index: 1;
    color: var(--green);
    font-weight: 500;
    line-height: 1.15;
  }
  .card--front .brand {
    left: 240px;
    top: 150px;
    font-size: 25px;
  }
  .card--front .brand small {
    display: block;
    font-size: 12px;
    letter-spacing: .6px;
    margin-top: 4px;
  }
  .brand-dot {
    display: inline-block;
    width: 10px; height: 10px;
    border-radius: 50%;
    background: var(--green);
    margin-right: 6px;
    vertical-align: middle;
  }
  .card--back .brand {
    left: 26px;
    top: 24px;
    font-size: 15px;
  }
  .card--back .brand small {
    display: block;
    font-size: 8px;
    letter-spacing: .5px;
    margin-left: 16px;
  }

  .contact {
    position: absolute;
    z-index: 1;
    left: 26px;
    top: 84px;
    font-family: "Roboto", sans-serif;
    color: var(--grey);
    font-size: 10.5px;
    line-height: 1.55;
  }
  .contact .name {
    font-family: "Montserrat", sans-serif;
    color: var(--green);
    font-size: 15px;
    font-weight: 400;
    letter-spacing: .2px;
  }
  .contact .name b { font-weight: 700; }
  .contact .role { font-size: 11px; margin-bottom: 4px; }
  .contact .label { color: var(--brown); font-weight: 700; font-family: "Montserrat", sans-serif; }
  .contact .web {
    color: var(--brown);
    letter-spacing: 3px;
    margin-top: 6px;
    font-size: 10px;
  }

  .hours {
    position: absolute;
    z-index: 1;
    right: 26px;
    top: 92px;
    font-family: "Roboto", sans-serif;
    color: var(--grey);
    font-size: 11px;
    line-height: 1.6;
    text-align: right;
  }
</style>
</head>
<body>

<section class="card card--front">
  <div class="artwork" role="img" aria-label="Illustration of a tree with a cat and a dog"></div>
  <div class="brand"><span class="brand-dot"></span>Maple Hollow<small>VETERINARY HOSPITAL</small></div>
</section>

<section class="card card--back">
  <div class="artwork" role="img" aria-label="Illustration of a tree with a cat and a dog"></div>

  <div class="brand"><span class="brand-dot"></span>Maple Hollow<small>VETERINARY HOSPITAL</small></div>

  <div class="contact">
    <p class="name">DANIEL R. <b>ASHFORD</b></p>
    <p class="role">Doctor</p>
    <p><span class="label">P:</span> (555) 284-1960</p>
    <p><span class="label">E:</span> info@tqrn.net</p>
    <p>4820 Cedar Ridge Lane,<br>Brookfield, TX 75010</p>
    <p class="web">www.tqrn.net</p>
  </div>

  <div class="hours">
    <p>Monday To Friday : 7:00am – 6:00pm</p>
    <p>Saturday: 8:00am – 12:00pm</p>
    <p>Sunday: Closed</p>
  </div>
</section>

</body>
</html>
```